Photography Business, Business Card

Looking for a unique cutting edge card that takes advantage of the latest printing technologies. Please review this site for all the options they office: https://plumeprints.example. If you can think it they can do it. And if you have an idea and do not know if they can do it, I will check into it.
Updates

Target Market(s)

People and places I took images of and future clients.

Industry/Entity Type

Photography

Contact Information for Business Card

Name, cell & email. Colin Hartley, chartley@kvnphoto.example, 318-742-9061

Colors

Designer to choose only greyscale colors for use in the design.

Requirements
Must have
• 100% cutting edge. Is so great, those I hand it to always show it to someone else. A piece of art.
Nice to have
• Blacks, silvers, greys, some red. Maybe other colors?

```html
<!DOCTYPE html>
<html lang="en">
<head>
<meta charset="utf-8">
<title>Colin Hartley Photography – Business Card</title>
<link rel="stylesheet" href="https://fonts.googleapis.com/css2?family=Jost:wght@400;500;600&display=swap">
<style>
  :root {
    --page-bg: #eceeed;
    --card-bg: #2a2928;
    --ink-light: #f2f2f2;
    --ink-muted: #8a8a8a;
    --note-ink: #2b2b2b;
    --silver-hi: #f1f1f0;
    --silver-lo: #5e5e5e;
  }
  * { margin: 0; padding: 0; box-sizing: border-box; }
  html, body { width: 848px; height: 1200px; overflow: hidden; }
  body {
    background: var(--page-bg);
    font-family: "Jost", sans-serif;
    position: relative;
  }
  .card {
    position: absolute;
    left: 212px;
    top: 420px;
    width: 600px;
    height: 360px;
    background: var(--card-bg);
    border-radius: 20px;
    overflow: hidden;
  }
  .card__phone {
    position: absolute;
    left: 42px;
    top: 30px;
    color: var(--ink-light);
    font-weight: 600;
    font-size: 16px;
    letter-spacing: 0.3px;
  }
  .card__brand {
    position: absolute;
    right: 38px;
    top: 58px;
    text-align: right;
    color: var(--ink-muted);
  }
  .card__brand-name {
    font-weight: 400;
    font-size: 32px;
    line-height: 1;
  }
  .card__brand-tag {
    margin-top: 4px;
    font-size: 8px;
    letter-spacing: 2.6px;
  }
  .card__email {
    position: absolute;
    right: 36px;
    bottom: 28px;
    color: var(--ink-light);
    font-weight: 600;
    font-size: 16px;
  }
  .card__mark {
    position: absolute;
    left: -10px;
    top: 78px;
    width: 312px;
    height: 312px;
  }
  .note {
    position: absolute;
    left: 20px;
    width: 215px;
    color: var(--note-ink);
    font-size: 15px;
    padding-bottom: 3px;
    border-bottom: 1px solid var(--note-ink);
  }
  .note--foil { top: 545px; }
  .note--cut { top: 608px; }
</style>
</head>
<body>
  <p class="note note--foil">Silver Leaf Printing</p>
  <p class="note note--cut">White posion is cutting</p>

  <section class="card" aria-label="Business card front">
    <p class="card__phone">318-742-9061</p>
    <div class="card__brand">
      <p class="card__brand-name">Colin Hartley</p>
      <p class="card__brand-tag">PHOTOGRAPHY</p>
    </div>
    <svg class="card__mark" viewBox="0 0 312 312" role="img" aria-label="Silver leaf and die-cut brand mark area">
      <defs>
        <linearGradient id="silverFoil" x1="0" y1="0" x2="1" y2="1">
          <stop offset="0" stop-color="var(--silver-lo)"/>
          <stop offset="0.55" stop-color="var(--silver-hi)"/>
          <stop offset="1" stop-color="var(--silver-lo)"/>
        </linearGradient>
      </defs>
      <circle cx="156" cy="156" r="150" fill="url(#silverFoil)"/>
    </svg>
    <p class="card__email">chartley@kvnphoto.example</p>
  </section>
</body>
</html>
```